Brochure Design Project for Brockwin and Daughters Lumber

We are after an executive high-end trifold brochure to be sent to new customers. Please refer to document attached ('brochure notes') for the details.

Target Market(s)

Renovators, Wives, Architects, Builders

Requirements
Must have
• Back of brochure must have a map and contact details.

Must relate to the feel of our website ... brockwinanddaughterslumber.net

Nice to have
• A unique design - something unlike regular brochures.

Developed using Adobe Photoshop or InDesign

```html
<!DOCTYPE html>
<html lang="en">
<head>
<meta charset="utf-8">
<title>Brockwin and Daughters Lumber – Trifold Brochure</title>
<link rel="stylesheet" href="https://fonts.googleapis.com/css2?family=Arvo:wght@400;700&family=Open+Sans:wght@400;600&display=swap">
<style>
  :root {
    --band: #38332a;
    --panel-dark: rgba(52, 52, 38, 0.88);
    --panel-olive: rgba(70, 72, 52, 0.9);
    --ink-light: #ecebe2;
    --ink-soft: #d9d8cc;
    --brand-green: #7fb53f;
    --forest-deep: #1f3a18;
    --forest-mid: #3f6b26;
    --forest-light: #7da04a;
    --tray-top: #c4c7c7;
    --tray-bottom: #dcd8c6;
    --frame: #e8e5d8;
    --box: #3a3429;
    --map: #dfe0dc;
    --label: #1b1b1b;
  }
  * { box-sizing: border-box; margin: 0; padding: 0; }
  html, body { width: 1200px; height: 940px; overflow: hidden; background: #ffffff; }
  body { position: relative; font-family: "Open Sans", sans-serif; color: var(--ink-light); }

  .sheet { position: absolute; overflow: hidden; }
  .spread { width: 631px; }
  .single { width: 315px; }
  .front { top: 13px; height: 446px; }
  .back { top: 480px; height: 446px; }
  .left-x { left: 13px; }
  .right-x { left: 667px; }

  .side-label {
    position: absolute; left: 1037px; font-family: "Open Sans", sans-serif;
    font-size: 46px; color: var(--label); font-weight: 400;
  }

  .forest {
    position: absolute; left: 0; top: 0; right: 0;
    background:
      radial-gradient(ellipse at 50% 30%, rgba(170, 200, 110, 0.55), transparent 60%),
      linear-gradient(180deg, var(--forest-mid) 0%, var(--forest-light) 45%, var(--forest-mid) 75%, var(--forest-deep) 100%);
  }
  .band { position: absolute; left: 0; right: 0; bottom: 0; background: var(--band); }

  .column { position: absolute; top: 0; padding: 27px 10px 0 20px; }
  .column.dark { background: var(--panel-dark); }
  .column.olive { background: var(--panel-olive); }

  .col-title { font-family: "Arvo", serif; font-size: 9.5px; margin-bottom: 1px; }
  .col-body { font-size: 7.3px; line-height: 9.5px; color: var(--ink-soft); }
  .col-body + .col-body { margin-top: 9px; }
  .col-item { font-family: "Arvo", serif; font-size: 9.3px; line-height: 10px; margin-top: 11px; letter-spacing: 0.2px; }

  .tagline {
    position: absolute; text-align: center; font-size: 9.6px; line-height: 12.4px;
    font-weight: 600; color: #fff; letter-spacing: 0.2px;
  }

  .question { position: absolute; text-align: center; font-family: "Arvo", serif; color: var(--ink-light); }
  .question .small { font-size: 11.5px; line-height: 13px; }
  .question .big { font-size: 16.5px; line-height: 17px; }
  .question .or { font-size: 9px; line-height: 12px; }

  .wordmark {
    position: absolute; display: flex; flex-direction: column; align-items: center; gap: 6px;
    font-family: "Arvo", serif; font-weight: 700; color: var(--brand-green);
    text-align: center; font-size: 11px; line-height: 12px;
  }
  .wordmark .dot { width: 34px; height: 34px; border-radius: 50%; background: var(--brand-green); }
  .wordmark.inline { flex-direction: row; gap: 8px; font-size: 13px; }
  .wordmark.inline .dot { width: 22px; height: 22px; }

  .contact { position: absolute; font-size: 7.4px; line-height: 8.7px; color: var(--ink-soft); }
  .contact dl { margin-top: 8px; display: grid; grid-template-columns: 22px auto; }
  .contact dd::before { content: ": "; }

  .map { position: absolute; background: var(--map); border: 3px solid #f4f3ee; }

  .tray-top { position: absolute; left: 0; top: 0; width: 631px; height: 197px; background: var(--tray-top); }
  .tray-bottom { position: absolute; left: 0; top: 197px; width: 631px; height: 198px; background: var(--tray-bottom); }
  .photo { position: absolute; border: 2px solid var(--frame); }
  .photo.deck { background: linear-gradient(180deg, #9bb3c6 0%, #6d8fa3 30%, #b08e7b 55%, #a07c68 100%); }
  .photo.floor { background: linear-gradient(135deg, #7a3d22 0%, #a35a32 45%, #5c2c18 100%); }
  .photo.fence { background: linear-gradient(160deg, #d9d6cf 0%, #b8774f 35%, #9c5a36 70%, #c9c5bb 100%); }
  .photo.kitchen { background: linear-gradient(180deg, #d9d0c0 0%, #b9ad9a 50%, #8a5a34 75%, #6e4424 100%); }

  .feature {
    position: absolute; left: 165px; width: 301px; background: var(--box);
    text-align: center; padding: 9px 10px 0;
  }
  .feature h2 { font-family: "Arvo", serif; font-weight: 400; font-size: 11px; letter-spacing: 0.3px; margin-bottom: 3px; }
  .feature p { font-size: 6.3px; line-height: 8.2px; color: var(--ink-soft); }
  .feature p + p { margin-top: 5px; }
</style>
</head>
<body>

<!-- FRONT: outside spread -->
<section class="sheet spread front left-x">
  <div class="forest" style="height:325px" role="img" aria-label="Photograph of a tall green forest with sunlit undergrowth"></div>

  <div class="column dark" style="left:0;width:157px;height:325px;padding-left:21px">
    <h3 class="col-title">About Us</h3>
    <p class="col-body">Welcome to Brockwin and Daughters Lumber, from the family that brought you Grainwell Timbers. We understand that deciding on the perfect project for home comes with lots of questions. We're the experts not only in timber, but design, engineering and construction. Be it a little fence or the largest house, our friendly team is here to help.</p>
    <p class="col-body">We invite you to take your time looking over our website. We hope you find some inspiration to create your own masterpiece at your place. Don't forget we're only a phone call away and we're more than happy to assist.</p>
  </div>

  <p class="tagline" style="left:157px;width:317px;top:265px">We are modern timber suppliers specializing in decks, hardwood floors and external cladding. We provide high end service to builders, DIY and tradesmen.</p>

  <div class="column olive" style="left:474px;width:157px;height:325px;padding-left:20px">
    <h3 class="col-title">Want Cash?</h3>
    <p class="col-body">Become a renovation star! If you allow us to take photos, video or leave a sign, we will reward you with $50 cash for every order taken from interest in your home improvement.</p>
    <p class="col-item">We can come to you for free measure and quote.</p>
    <p class="col-item">Design advise</p>
    <p class="col-item">Can organize full installation</p>
    <p class="col-item">Feel free to use any info or pictures from our website</p>
  </div>

  <div class="band" style="height:121px">
    <div class="question" style="left:18px;width:124px;top:29px">
      <div class="small">Looking for something</div>
      <div class="big">different</div>
      <div class="or">or</div>
      <div class="big">unique?</div>
    </div>
    <div class="wordmark" style="left:170px;width:110px;top:18px">
      <span class="dot"></span>
      <span>Brockwin &amp; Daughters Lumber</span>
    </div>
    <div class="contact" style="left:289px;top:44px">
      <p>Unit 7 / 23 Ridgeway Road<br>HOLLOW PINES 4120</p>
      <dl>
        <dt>Call</dt><dd>1300 555 018 | (07) 5550 1234</dd>
        <dt>Fax</dt><dd>(07) 5550 4321</dd>
        <dt>Email</dt><dd>info@brockwinanddaughterslumber.com.au</dd>
        <dt>Web</dt><dd>http://brockwinanddaughterslumber.net</dd>
      </dl>
    </div>
    <div class="map" style="left:482px;top:6px;width:138px;height:107px" role="img" aria-label="Street map showing the yard location"></div>
  </div>
</section>

<!-- FRONT: cover panel -->
<section class="sheet single front right-x">
  <div class="forest" style="height:325px" role="img" aria-label="Photograph of a tall green forest with sunlit undergrowth"></div>
  <p class="tagline" style="left:0;width:315px;top:265px">We are modern timber suppliers specializing in decks, hardwood floors and external cladding. We provide high end service to builders, DIY and tradesmen.</p>
  <div class="band" style="height:121px">
    <div class="wordmark" style="left:18px;width:110px;top:18px">
      <span class="dot"></span>
      <span>Brockwin &amp; Daughters Lumber</span>
    </div>
    <div class="contact" style="left:132px;top:44px">
      <p>Unit 7 / 23 Ridgeway Road<br>HOLLOW PINES 4120</p>
      <dl>
        <dt>Call</dt><dd>1300 555 018 | (07) 5550 1234</dd>
        <dt>Fax</dt><dd>(07) 5550 4321</dd>
        <dt>Email</dt><dd>info@brockwinanddaughterslumber.com.au</dd>
        <dt>Web</dt><dd>http://brockwinanddaughterslumber.net</dd>
      </dl>
    </div>
  </div>
</section>

<div class="side-label" style="top:208px">front</div>

<!-- BACK: inside spread -->
<section class="sheet spread back left-x">
  <div class="tray-top"></div>
  <div class="tray-bottom"></div>

  <div class="photo deck" style="left:6px;top:5px;width:148px;height:186px" role="img" aria-label="Photograph of a composite timber deck beside a waterfront railing"></div>
  <div class="photo floor" style="left:479px;top:6px;width:145px;height:184px" role="img" aria-label="Photograph of a polished hardwood floor with a round rug"></div>
  <div class="photo fence" style="left:6px;top:204px;width:148px;height:185px" role="img" aria-label="Photograph of a slatted timber feature fence"></div>
  <div class="photo kitchen" style="left:479px;top:204px;width:145px;height:185px" role="img" aria-label="Photograph of a kitchen with timber flooring"></div>

  <article class="feature" style="top:6px;height:85px">
    <h2>COMPOSITE TIMBER</h2>
    <p>Timber decks and screening are very popular but require constant maintenance. This timber-like product gives the look of timber, but with minimal upkeep.</p>
    <p>The 'greenest of green' … This timber-like product will give you the look you're after, without needing to oil …. EVER!</p>
  </article>

  <article class="feature" style="top:103px;height:87px">
    <h2>KESTREL TIMBER</h2>
    <p>The products include decking, flooring, structural timber and step treads.</p>
    <p>Benefits of the Kestrel Timber species:<br>Durability Class 1 - no need to treat with nasty chemicals<br>Environmentally sustainable - fully certified<br>Strong | Beautiful<br>Wide range of uses available - decking, step treads, posts, joists.</p>
  </article>

  <article class="feature" style="top:203px;height:88px;padding-top:24px">
    <h2>FEATURE FENCING</h2>
    <p>We are able to supply you with designer fencing fully installed for much less than you think. Endless combinations available.<br>Call for an obligation-free quote today.</p>
  </article>

  <article class="feature" style="top:303px;height:86px;padding-top:18px">
    <h2>TRADITIONAL TIMBER AND BAMBOO FLOORING</h2>
    <p>Bamboo flooring is becoming an increasingly popular choice for many homeowners, architects, builders and interior designers who are looking for an environmental alternative to timber flooring that is a stylish, hard wearing, pre-finished flooring system.</p>
  </article>

  <div class="band" style="height:51px">
    <div class="wordmark inline" style="left:0;right:0;top:16px;justify-content:center">
      <span class="dot"></span>
      <span>Brockwin &amp; Daughters Lumber</span>
    </div>
  </div>
</section>

<!-- BACK: flap panels -->
<section class="sheet single back right-x">
  <div class="forest" style="height:446px" role="img" aria-label="Photograph of a dim forest behind the text panels"></div>

  <div class="column olive" style="left:0;width:157px;height:446px;padding-left:21px;padding-top:25px;border-right:1px solid rgba(255,255,255,0.15)">
    <h3 class="col-title">Want Cash?</h3>
    <p class="col-body">Become a renovation star! If you allow us to take photos, video or leave a sign, we will reward you with $50 cash for every order taken from interest in your home improvement.</p>
    <p class="col-item">We can come to you for free measure and quote.</p>
    <p class="col-item">Design advise</p>
    <p class="col-item">Can organize full installation</p>
    <p class="col-item">Feel free to use any info or pictures from our website</p>
    <div class="map" style="left:11px;top:330px;width:136px;height:106px" role="img" aria-label="Street map showing the yard location"></div>
  </div>

  <div class="column olive" style="left:157px;width:158px;height:446px;padding-left:20px;padding-top:25px">
    <h3 class="col-title">About Us</h3>
    <p class="col-body">Welcome to Brockwin and Daughters Lumber, from the family that brought you Grainwell Timbers. We understand that deciding on the perfect project for home comes with lots of questions. We're the experts not only in timber, but design, engineering and construction. Be it a little fence or the largest house, our friendly team is here to help.</p>
    <p class="col-body">We invite you to take your time looking over our website. We hope you find some inspiration to create your own masterpiece at your place. Don't forget we're only a phone call away and we're more than happy to assist.</p>
    <div class="question" style="left:12px;width:134px;top:355px">
      <div class="small">Looking for something</div>
      <div class="big">different</div>
      <div class="or">or</div>
      <div class="big">unique?</div>
    </div>
  </div>
</section>

<div class="side-label" style="top:672px">back</div>

</body>
</html>
```